Business Card Design Project

Hello
I want a Simple Business card that uses the company logo that is easily reasonable but looks professional as I am an IT Services company and would look to share these cards with prospective clients.
The details are:
Kestrel Arc Solutions
14 Morrow Lane
Birmingham
B7 4QX
Telephone 0845 217 6640
I would like my name Oliver Hastings and my title Director on the card.
Target Market(s)
IT Professionals
Industry/Entity Type
Business

```html
<!DOCTYPE html>
<html lang="en">
<head>
<meta charset="utf-8">
<title>Kestrel Arc Solutions – Business Card</title>
<link href="https://fonts.googleapis.com/css2?family=Questrial&display=swap" rel="stylesheet">
<style>
  :root {
    --page-bg: #ecebe8;
    --card-white: #ffffff;
    --charcoal: #4a4a4c;
    --leaf-green: #d3e183;
    --sage-green: #c6d27b;
    --logo-dot: #a9c95a;
    --ink: #3b3b3b;
    --brand-white: #ffffff;
  }
  html, body {
    margin: 0;
    padding: 0;
    width: 1200px;
    height: 1000px;
    overflow: hidden;
    background: var(--page-bg);
  }
  .canvas {
    position: relative;
    width: 1200px;
    height: 1000px;
    display: flex;
    align-items: center;
    justify-content: center;
  }
  .business-card {
    display: block;
    width: 1050px;
    height: 665px;
    box-shadow: 0 6px 18px rgba(0, 0, 0, 0.18);
  }
  .card-face { fill: var(--card-white); }
  .header-bubble { fill: var(--charcoal); }
  .bubble-address, .bubble-name { fill: var(--leaf-green); }
  .bubble-phone { fill: var(--sage-green); }
  .brand-dot { fill: var(--logo-dot); }
  .brand-name {
    font-family: "Questrial", sans-serif;
    font-size: 30px;
    fill: var(--brand-white);
    letter-spacing: 0.5px;
  }
  .card-text {
    font-family: "Questrial", sans-serif;
    font-size: 17px;
    fill: var(--ink);
    letter-spacing: 0.4px;
  }
</style>
</head>
<body>
<main class="canvas">
  <svg class="business-card" viewBox="0 0 704 446" xmlns="http://www.w3.org/2000/svg" aria-label="Kestrel Arc Solutions business card">
    <defs>
      <clipPath id="card-clip">
        <rect width="704" height="446"/>
      </clipPath>
    </defs>
    <g clip-path="url(#card-clip)">
      <rect class="card-face" width="704" height="446"/>

      <path class="header-bubble"
            d="M0 0 H704 V82 C640 200 500 236 360 236 C300 236 250 232 200 226 L89 262 L97 152 C40 125 5 90 0 52 Z"/>

      <g class="brand">
        <circle class="brand-dot" cx="258" cy="66" r="24"/>
        <text class="brand-name" x="258" y="138" text-anchor="middle">Kestrel Arc Solutions</text>
      </g>

      <g class="bubble-group address">
        <path class="bubble-address" d="M132 352 L127 408 L178 378 Z"/>
        <ellipse class="bubble-address" cx="215" cy="302" rx="122" ry="80"/>
        <text class="card-text" text-anchor="end">
          <tspan x="297" y="287">Kestrel Arc Solutions</tspan>
          <tspan x="297" y="309">14 Morrow Lane</tspan>
          <tspan x="297" y="331">Birmingham</tspan>
          <tspan x="297" y="353">B7 4QX</tspan>
        </text>
      </g>

      <g class="bubble-group contact-name">
        <path class="bubble-name" d="M592 262 L594 305 L552 286 Z"/>
        <ellipse class="bubble-name" cx="512" cy="207" rx="113" ry="88"/>
        <text class="card-text" text-anchor="end">
          <tspan x="585" y="208">Oliver Hastings</tspan>
          <tspan x="585" y="229">Director</tspan>
        </text>
      </g>

      <g class="bubble-group telephone">
        <ellipse class="bubble-phone" cx="484" cy="377" rx="122" ry="80"/>
        <text class="card-text" text-anchor="end">
          <tspan x="552" y="371">Telephone</tspan>
          <tspan x="552" y="392">0845 217 6640</tspan>
        </text>
      </g>
    </g>
  </svg>
</main>
</body>
</html>
```